Hi, Looking for an upgraded business card to the aged one attached. Open to suggestions and no real limitations, but if your going to use a picture of a taxi i think it should be vector based rather than a full color picture. I've uploaded a 2 pictures of the type of taxi which is a Torvane K5 in white. The taxi markings look like the pink one in the picture but to be clear his is white. The taxi is in Bermuda so if you wanted to include something island based that's ok as well but not required. The other thing he wanted to keep on there was the bermuda police crest, with the retired police office incorporated somehow.

Requirements
Must have
• Bermuda Taxi Operator
Retired Police Officer
Police Crest
Taxi #
Email
Mobile Number

```html
<!DOCTYPE html>
<html lang="en">
<head>
<meta charset="utf-8">
<title>Bermuda Taxi Operator – Business Card</title>
<link href="https://fonts.googleapis.com/css2?family=Rubik:wght@400;500;700&family=Oswald:wght@700&display=swap" rel="stylesheet">
<style>
  :root {
    --navy: #172c5b;
    --ink: #2b2b2b;
    --card: #ffffff;
    --backdrop: #c9cbb0;
    --van-light: #f4f5f7;
    --van-mid: #d9dce2;
  }
  * { margin: 0; padding: 0; box-sizing: border-box; }
  html, body { width: 1200px; height: 900px; overflow: hidden; }
  body {
    background: var(--backdrop);
    font-family: "Rubik", Arial, sans-serif;
    position: relative;
  }
  .business-card {
    position: absolute;
    left: 75px; top: 150px;
    width: 1050px; height: 600px;
    background: var(--card);
    box-shadow: 0 12px 30px rgba(0,0,0,0.18);
    overflow: hidden;
  }
  .contact { position: absolute; left: 80px; top: 170px; }
  .contact__name {
    font-weight: 700; font-size: 46px; color: var(--navy); line-height: 1;
  }
  .contact__title {
    font-size: 25px; color: var(--ink); margin-top: 8px;
  }
  .contact__phone {
    font-weight: 700; font-size: 40px; color: var(--navy); margin-top: 44px; line-height: 1;
  }
  .contact__email {
    font-size: 28px; color: var(--ink); margin-top: 8px;
  }
  .vehicle-illustration {
    position: absolute; left: 470px; top: 40px;
    width: 520px; height: 290px;
    border-radius: 40px 90px 30px 30px;
    background: linear-gradient(160deg, var(--van-light), var(--van-mid));
  }
  .trade-band {
    position: absolute; left: 0; top: 380px;
    width: 100%; height: 88px;
    background: var(--navy);
  }
  .trade-band__label {
    position: absolute; left: 70px; top: 50%;
    transform: translateY(-50%);
    font-family: "Oswald", "Arial Narrow", sans-serif;
    font-weight: 700; font-size: 62px; letter-spacing: 1px;
    color: #fff; line-height: 1;
  }
  .agency-mark {
    position: absolute; left: 780px; top: 300px;
    width: 230px; height: 230px;
    border-radius: 50%;
    background: var(--card);
    display: flex; align-items: center; justify-content: center;
    text-align: center;
    font-weight: 700; font-size: 26px; line-height: 1.2;
    color: var(--navy);
    padding: 20px;
  }
  .taxi-number {
    position: absolute; left: 80px; top: 510px;
    font-size: 32px; color: var(--ink);
  }
</style>
</head>
<body>
  <main class="business-card">
    <div class="vehicle-illustration" role="img" aria-label="Vector drawing of a white Torvane K5 taxi van with roof sign and taxi number on the side"></div>

    <section class="contact">
      <h1 class="contact__name">Derrin Calloway</h1>
      <p class="contact__title">Retired Police Officer</p>
      <p class="contact__phone">1-441-555-0142</p>
      <p class="contact__email">dcalloway@mailbay.net</p>
    </section>

    <div class="trade-band">
      <span class="trade-band__label">BERMUDA TAXI OPERATOR</span>
    </div>

    <div class="agency-mark">Coral Isle Constabulary</div>

    <p class="taxi-number">Taxi #T2417</p>
  </main>
</body>
</html>
```